Letterhead design for ZENTORA company

I need an A4 letterhead design for my company "Zentora Electrical Products". I need the letterhead to match my current logo and business card designs. I would like it to be colourful and match the design of the business card in terms of the flowing line of colour where the information is.  

Target Market(s)

Adults aged 20 - 50 Upper middle class.

Industry/Entity Type

It Company

Requirements
Must have
• Must be A4 size and match my current logo and business card designs. Must be clean simple and eye catching.

• Must have the following information

• Zentora Electrical Products LTD
• 7 Ardley Close
• Chiswick
• London
• England
• W9 3QX
• Company No. 05316429
• VAT No. GB 627150384

• Telephone: 02081594360
• Mobile: 07815062247
• Email: info@zentora-goods.co.uk
Nice to have
• nice to have a wave of colour like the business card.
Should not have
• Should not be a different colour scheme to the business card and logo design.

```html
<!DOCTYPE html>
<html lang="en">
<head>
<meta charset="utf-8">
<title>Zentora Electrical Products – Stationery</title>
<link rel="stylesheet" href="https://fonts.googleapis.com/css2?family=Quicksand:wght@400;500&family=Open+Sans:wght@400&display=swap">
<style>
  :root {
    --brand-teal: #3ed8bf;
    --wash-strong: rgba(62, 216, 191, 0.20);
    --wash-soft: rgba(62, 216, 191, 0.08);
    --ink: #1e1e1e;
    --paper: #ffffff;
    --canvas: #ffffff;
    --sheet-edge: #d9d9d9;
    --sheet-shadow: rgba(0, 0, 0, 0.28);
  }
  * { margin: 0; padding: 0; box-sizing: border-box; }
  html, body {
    width: 1200px;
    height: 1105px;
    overflow: hidden;
    background: var(--canvas);
  }
  .stationery-set {
    position: relative;
    width: 1200px;
    height: 1105px;
  }
  .sheet {
    position: absolute;
    overflow: hidden;
    background: var(--paper);
    border: 1px solid var(--sheet-edge);
    box-shadow: 3px 4px 4px var(--sheet-shadow);
  }

  /* Soft colour wash behind content */
  .colour-wash {
    position: absolute;
    border-radius: 50%;
    background: radial-gradient(circle at 50% 50%,
      var(--wash-strong) 0%,
      var(--wash-strong) 35%,
      var(--wash-soft) 62%,
      rgba(62, 216, 191, 0) 72%);
  }

  .brand-name {
    position: absolute;
    font-family: "Quicksand", sans-serif;
    font-weight: 400;
    color: var(--brand-teal);
    letter-spacing: 0;
    line-height: 1;
    font-size: 34px;
  }
  .brand-tagline {
    position: absolute;
    font-family: "Quicksand", sans-serif;
    font-weight: 500;
    color: var(--brand-teal);
    line-height: 1;
    letter-spacing: 0.4px;
    font-size: 14.5px;
  }

  /* Letterhead */
  .letterhead {
    left: 52px;
    top: 211px;
    width: 614px;
    height: 792px;
  }
  .letterhead .colour-wash {
    left: 6px;
    top: 110px;
    width: 600px;
    height: 580px;
  }
  .letterhead .brand-name { left: 34px; top: 16px; }
  .letterhead .brand-tagline { left: 35px; top: 53px; }
  .letterhead-footer {
    position: absolute;
    left: 0;
    right: 0;
    top: 726px;
    text-align: center;
    font-family: "Open Sans", sans-serif;
    font-size: 9.3px;
    line-height: 15px;
    color: var(--ink);
  }
  .letterhead-footer .sep { padding: 0 3px; }

  /* Envelope */
  .envelope {
    left: 412px;
    top: 53px;
    width: 686px;
    height: 298px;
  }
  .envelope .colour-wash {
    left: 320px;
    top: -20px;
    width: 420px;
    height: 400px;
  }
  .envelope .brand-name { left: 34px; top: 16px; }
  .envelope .brand-tagline {
    left: 35px;
    top: 54px;
    padding-bottom: 4px;
    border-bottom: 1px solid var(--ink);
    width: 145px;
  }
  .return-address {
    position: absolute;
    left: 35px;
    top: 77px;
    font-family: "Open Sans", sans-serif;
    font-size: 8.8px;
    line-height: 12px;
    color: var(--ink);
    font-style: normal;
  }
</style>
</head>
<body>
  <main class="stationery-set">
    <section class="sheet letterhead" aria-label="Letterhead">
      <div class="colour-wash" role="img" aria-label="Large soft teal brand decoration"></div>
      <div class="brand-name">ZENTORA</div>
      <div class="brand-tagline">Electrical Products</div>
      <footer class="letterhead-footer">
        <p>7 Ardley Close<span class="sep">•</span>Chiswick, London, England W9 3QX<span class="sep">•</span>Company No. 05316429<span class="sep">•</span>VAT No. GB 627150384</p>
        <p>Phone: 02081594360<span class="sep">•</span>Mobile: 07815062247<span class="sep">•</span>E-mail: info@zentora-goods.co.uk<span class="sep">•</span>Website: www.zentora-goods.co.uk</p>
      </footer>
    </section>

    <section class="sheet envelope" aria-label="DL envelope">
      <div class="colour-wash" role="img" aria-label="Large soft teal brand decoration"></div>
      <div class="brand-name">ZENTORA</div>
      <div class="brand-tagline">Electrical Products</div>
      <address class="return-address">
        7 Ardley Close, Chiswick<br>
        London, England W9 3QX
      </address>
    </section>
  </main>
</body>
</html>
```